Saltmarsh Valley Lending Flyer

I would like our main long logo with the bird and words Saltmarsh Valley Lending with pictures of what we finance along the bottom.
Car , 4x4 , boat, excavator , Cash Loans and houses
Needs to look good on leaflet and large signage.
Simple but cool looking so it stands out.

```html
<!DOCTYPE html>
<html lang="en">
<head>
<meta charset="utf-8">
<title>Saltmarsh Valley Lending Flyer</title>
<link href="https://fonts.googleapis.com/css2?family=Cinzel:wght@500;700&family=Lato:wght@400;700&display=swap" rel="stylesheet">
<style>
  :root {
    --orange: #d9772b;
    --ink: #1c1c1c;
    --panel: #262626;
    --paper: #ffffff;
    --backdrop: #e6e6e6;
    --soft-text: #e9e9e9;
  }
  * { box-sizing: border-box; margin: 0; padding: 0; }
  html, body { width: 1200px; height: 1200px; overflow: hidden; }
  body { background: var(--backdrop); font-family: "Lato", sans-serif; position: relative; }

  .flyer {
    position: absolute; left: 210px; top: 35px; width: 780px; height: 1130px;
    background: var(--paper); overflow: hidden;
    box-shadow: 0 6px 24px rgba(0,0,0,.18);
  }

  .brand {
    position: absolute; top: 58px; left: 0; width: 100%;
    display: flex; justify-content: center; align-items: center; gap: 12px;
  }
  .brand-mark { width: 30px; height: 30px; border-radius: 50%; background: var(--orange); }
  .brand-name {
    font-family: "Cinzel", serif; font-weight: 500; font-size: 22px;
    color: var(--ink); letter-spacing: 1px;
  }

  .headline { position: absolute; top: 112px; width: 100%; text-align: center; font-family: "Cinzel", serif; font-weight: 700; line-height: 1.02; }
  .headline-lead { color: var(--ink); font-size: 50px; }
  .headline-main { color: var(--orange); font-size: 60px; }

  .hero { position: absolute; top: 300px; left: 0; width: 780px; height: 520px; }

  .services-tab {
    position: absolute; top: 826px; left: 40px; width: 220px; height: 46px;
    background: var(--orange); color: #fff; font-weight: 700; font-size: 28px;
    padding: 8px 0 0 28px; letter-spacing: .5px;
  }
  .services-panel {
    position: absolute; top: 872px; left: 40px; width: 740px; height: 190px;
    background: var(--panel); padding: 16px 30px 0 30px;
  }
  .services-intro { color: var(--soft-text); font-size: 14px; line-height: 1.35; max-width: 680px; }
  .service-list {
    list-style: none; display: grid; grid-template-columns: repeat(3, 1fr);
    row-gap: 14px; margin-top: 18px;
  }
  .service-item { display: flex; align-items: center; gap: 12px; color: #fff; font-size: 20px; }
  .service-icon {
    width: 40px; height: 40px; border-radius: 50%; background: var(--orange);
    display: flex; align-items: center; justify-content: center; flex: none;
  }
  .service-icon svg { width: 24px; height: 24px; }

  .contact-band {
    position: absolute; top: 1062px; left: 0; width: 780px; height: 68px;
    background: var(--orange); display: flex; justify-content: space-around; align-items: center;
    padding: 0 30px;
  }
  .contact-item { display: flex; align-items: center; gap: 9px; color: #fff; font-size: 17px; }
  .contact-item svg { width: 18px; height: 18px; }
</style>
</head>
<body>
<main class="flyer">
  <header class="brand">
    <span class="brand-mark"></span>
    <span class="brand-name">Saltmarsh Valley Lending</span>
  </header>

  <h1 class="headline">
    <span class="headline-lead">EXPERTS IN</span><br>
    <span class="headline-main">MORTGAGE BROKING<br>AND LENDING</span>
  </h1>

  <svg class="hero" viewBox="0 0 780 520">
    <defs>
      <linearGradient id="houseTones" x1="0" y1="0" x2="0" y2="1">
        <stop offset="0" stop-color="#4f8fd6"/>
        <stop offset=".35" stop-color="#cdb98a"/>
        <stop offset=".7" stop-color="#5f7d3a"/>
        <stop offset="1" stop-color="#a9a69c"/>
      </linearGradient>
      <linearGradient id="boatTones" x1="0" y1="0" x2="0" y2="1">
        <stop offset="0" stop-color="#b9d3ea"/><stop offset=".5" stop-color="#f2f4f6"/><stop offset="1" stop-color="#3f78a8"/>
      </linearGradient>
      <linearGradient id="carTones" x1="0" y1="0" x2="0" y2="1">
        <stop offset="0" stop-color="#cfc7b8"/><stop offset=".55" stop-color="#f5f5f5"/><stop offset="1" stop-color="#9a958c"/>
      </linearGradient>
      <linearGradient id="meetingTones" x1="0" y1="0" x2="1" y2="1">
        <stop offset="0" stop-color="#e9edf1"/><stop offset=".6" stop-color="#8a99ad"/><stop offset="1" stop-color="#2f3c55"/>
      </linearGradient>
    </defs>
    <circle cx="315" cy="268" r="246" fill="#fff" stroke="#ddd" stroke-width="1"/>
    <circle cx="315" cy="268" r="236" fill="var(--orange)"/>
    <circle cx="345" cy="240" r="222" fill="#fff"/>
    <circle role="img" aria-label="Photo of a modern two-storey home with garden" cx="345" cy="240" r="214" fill="url(#houseTones)"/>

    <circle cx="580" cy="80" r="66" fill="#fff"/>
    <circle role="img" aria-label="Photo of a motor cruiser on the water" cx="580" cy="80" r="58" fill="url(#boatTones)" stroke="var(--orange)" stroke-width="6"/>
    <circle cx="640" cy="225" r="66" fill="#fff"/>
    <circle role="img" aria-label="Photo of a white sports car" cx="640" cy="225" r="58" fill="url(#carTones)" stroke="var(--orange)" stroke-width="6"/>
    <circle cx="690" cy="385" r="72" fill="#fff"/>
    <circle role="img" aria-label="Photo of two business people reviewing documents" cx="690" cy="385" r="64" fill="url(#meetingTones)" stroke="var(--orange)" stroke-width="6"/>
  </svg>

  <div class="services-tab">SERVICES</div>
  <section class="services-panel">
    <p class="services-intro">There are a number of products on the market and it is important that you find a solution that best suits your needs and serviceability. We pride ourselves on our ability to get your loans settled! We have extensive experience in all things lending, including:</p>
    <ul class="service-list">
      <li class="service-item"><span class="service-icon"><svg viewBox="0 0 24 24" fill="#fff"><path d="M4 13l2-5h12l2 5v5H4z"/><circle cx="7.5" cy="18" r="2" fill="#d9772b" stroke="#fff" stroke-width="1.5"/><circle cx="16.5" cy="18" r="2" fill="#d9772b" stroke="#fff" stroke-width="1.5"/></svg></span>Car Loans</li>
      <li class="service-item"><span class="service-icon"><svg viewBox="0 0 24 24" fill="#fff"><rect x="3" y="8" width="18" height="9" rx="2"/><rect x="6" y="5" width="12" height="4"/><circle cx="7" cy="18" r="2.5"/><circle cx="17" cy="18" r="2.5"/></svg></span>4x4 Loans</li>
      <li class="service-item"><span class="service-icon"><svg viewBox="0 0 24 24" fill="#fff"><path d="M2 15h20l-3 4H5z"/><path d="M6 14l2-5h7l3 5z"/></svg></span>Boat Loans</li>
      <li class="service-item"><span class="service-icon"><svg viewBox="0 0 24 24" fill="#fff"><rect x="3" y="13" width="10" height="4"/><rect x="5" y="9" width="5" height="4"/><path d="M12 10l6-5 2 2-5 4z"/><path d="M18 7l3 6h-4z"/><rect x="2" y="17" width="12" height="3" rx="1.5"/></svg></span>Excavator Loans</li>
      <li class="service-item"><span class="service-icon"><svg viewBox="0 0 24 24" fill="#fff"><path d="M12 3l9 8h-3v9h-4v-6h-4v6H6v-9H3z"/></svg></span>Houses Loans</li>
      <li class="service-item"><span class="service-icon"><svg viewBox="0 0 24 24"><rect x="3" y="7" width="18" height="10" rx="1" fill="#fff"/><circle cx="12" cy="12" r="3" fill="#d9772b"/></svg></span>Cash Loans</li>
    </ul>
  </section>

  <footer class="contact-band">
    <span class="contact-item"><svg viewBox="0 0 24 24" fill="#fff"><path d="M6 2h4l2 5-3 2a11 11 0 006 6l2-3 5 2v4a2 2 0 01-2 2A18 18 0 014 4a2 2 0 012-2z"/></svg>08 5550 1284</span>
    <span class="contact-item"><svg viewBox="0 0 24 24"><rect x="2" y="5" width="20" height="14" fill="#fff"/><path d="M2 5l10 8 10-8" fill="none" stroke="#d9772b" stroke-width="2"/></svg>info@saltmarshlending.com.au</span>
    <span class="contact-item"><svg viewBox="0 0 24 24" fill="none" stroke="#fff" stroke-width="2"><circle cx="12" cy="12" r="9"/><path d="M3 12h18M12 3c3 3 3 15 0 18M12 3c-3 3-3 15 0 18"/></svg>www.saltmarshlending.com.au</span>
  </footer>
</main>
</body>
</html>
```